house selling company website

i need a website that is to get customers to let us sell their house within 30 days with no sales fees based in the uk. iv uploaded a design i like for the website i own i want a copy of this but for the different logo ect need the house buying logo i own to be changed to house selling company
it needs to be able to flash up to sell your house today contact box to collect their details such as property type, address, number of bedrooms, (estate agents valuation) , best price you can accept after they have seen the main section banner with advertising why use us.
the three reasons in the banner to use us needs to be
1: We will sell your house in 30 days and ensure we take a buyers fee for our service from the buyer meaning your buyer is secured unlike with most estate agents
2: We do not charge you any fees at all! our small fee is charged to the buyer
3: A huge network of investors and private buyers connecting many estate agents, auction houses, investors, and private buyers to ensure a fast sale.

```html
<!DOCTYPE html>
<html lang="en">
<head>
<meta charset="utf-8">
<title>Keystone Home Sales</title>
<link href="https://fonts.googleapis.com/css2?family=Montserrat:wght@400;500;600;700&display=swap" rel="stylesheet">
<style>
:root{
  --header-bg:#e3f3fc;
  --brand-blue:#1b8fd0;
  --hero-top:#0f74ad;
  --hero-bottom:#4ab0e0;
  --panel-blue:#3a9dd6;
  --green:#2fae3c;
  --ink:#111318;
  --muted:#3d434b;
  --section-bg:#e6e7ea;
  --card-bg:#e9eaed;
  --footer-bg:#17293a;
  --white:#ffffff;
}
*{box-sizing:border-box;margin:0;padding:0}
html,body{width:835px;height:1200px;overflow:hidden}
body{font-family:"Montserrat",sans-serif;color:var(--ink);background:var(--section-bg);position:relative}

.site-header{position:absolute;left:0;top:0;width:835px;height:59px;background:var(--header-bg);z-index:3}
.brand-tab{position:absolute;left:76px;top:40px;width:185px;height:46px;background:var(--white);border-radius:0 0 6px 6px;display:flex;align-items:center;justify-content:center;gap:6px;z-index:4}
.brand-tab .mark{width:12px;height:12px;background:var(--brand-blue)}
.brand-tab .name{font-size:14px;font-weight:500;color:var(--brand-blue)}
.main-nav{position:absolute;left:278px;top:24px;display:flex;gap:15px;font-size:10.5px;font-weight:600}
.btn-login,.btn-register{position:absolute;top:15px;height:30px;width:90px;border-radius:4px;color:var(--white);font-weight:700;font-size:11px;display:flex;align-items:center;gap:12px;padding-left:4px}
.btn-login{left:566px;background:var(--green)}
.btn-register{left:666px;background:var(--brand-blue)}
.btn-login .badge,.btn-register .badge{width:22px;height:22px;border-radius:50%;background:var(--white);display:flex;align-items:center;justify-content:center}

.hero{position:absolute;left:0;top:59px;width:835px;height:417px;background:linear-gradient(180deg,var(--hero-top),var(--hero-bottom))}
.hero-title{position:absolute;top:82px;width:100%;text-align:center;color:var(--white);font-weight:700;line-height:1.1}
.hero-title .line1{font-size:26px;display:block}
.hero-title .line2{font-size:31px;display:block}
.valuation-form{position:absolute;left:80px;top:159px;width:681px;height:80px;background:var(--panel-blue);border-radius:4px}
.form-title{position:absolute;left:7px;top:7px;color:var(--white);font-size:9px;font-weight:700;letter-spacing:.2px}
.field{position:absolute;top:26px;width:111px}
.field label{display:block;color:var(--white);font-size:7.5px;font-weight:600;margin-bottom:6px}
.field .input{height:20px;background:var(--white);border-radius:3px;font-size:7px;color:#555;padding:6px 5px;position:relative}
.field .input .caret{position:absolute;right:5px;top:7px;width:0;height:0;border-left:5px solid transparent;border-right:5px solid transparent;border-top:5px solid #333}
.btn-search{position:absolute;left:585px;top:41px;width:88px;height:20px;background:var(--green);border:1px solid var(--white);border-radius:4px;color:var(--white);font-size:7.5px;font-weight:600;text-align:center;line-height:18px}
.hero-scene{position:absolute;left:0;top:242px;width:835px;height:175px;background:linear-gradient(180deg,rgba(255,255,255,0.1),rgba(210,225,235,0.55) 55%,#9cc34a 80%,#d9e6ee)}

.why{position:absolute;left:0;top:476px;width:835px;height:467px;background:var(--section-bg)}
.skyline{position:absolute;left:0;top:264px;width:835px;height:203px;background:linear-gradient(180deg,rgba(200,202,206,0),#c9cacd)}
.why-title{position:absolute;top:60px;width:100%;text-align:center;font-size:26px;font-weight:700}
.reason-card{position:absolute;top:128px;width:202px;height:196px;background:var(--card-bg);box-shadow:0 2px 8px rgba(0,0,0,0.08);border-radius:3px}
.reason-card svg{position:absolute;left:56px;top:10px}
.reason-card h3{position:absolute;top:104px;width:100%;text-align:center;font-size:13px;font-weight:700}
.reason-card p{position:absolute;top:124px;left:12px;right:12px;text-align:center;font-size:7.3px;line-height:10.5px;color:var(--muted);font-weight:500}
.btn-contact{position:absolute;left:364px;top:363px;width:109px;height:31px;background:var(--brand-blue);border-radius:16px 4px 4px 16px;color:var(--white);font-size:11px;font-weight:700;display:flex;align-items:center;gap:6px;padding-left:3px}
.btn-contact .badge{width:25px;height:25px;border-radius:50%;background:var(--white);display:flex;align-items:center;justify-content:center}

.site-footer{position:absolute;left:0;top:943px;width:835px;height:257px;background:var(--footer-bg);color:var(--white)}
.footer-brand{position:absolute;left:79px;top:70px;display:flex;align-items:center;gap:6px}
.footer-brand .mark{width:13px;height:13px;background:var(--white)}
.footer-brand .name{font-size:14px;font-weight:500}
.social{position:absolute;left:83px;top:158px;display:flex;gap:18px}
.social span{width:28px;height:28px;border:1.5px solid var(--white);border-radius:50%}
.footer-col{position:absolute;top:68px}
.footer-col h4{font-size:17px;font-weight:700;margin-bottom:10px}
.footer-col ul{list-style:none;font-size:10px;line-height:20px}
.contact-list li{display:flex;align-items:flex-start;gap:6px}
.contact-list svg{margin-top:4px;flex:none}
.footer-rule{position:absolute;left:80px;top:220px;width:680px;height:1px;background:#c9d1d8}
.copyright{position:absolute;top:232px;width:100%;text-align:center;font-size:9.5px}
</style>
</head>
<body>

<header class="site-header">
  <nav class="main-nav">
    <span>Home</span><span>About Us</span><span>Services</span><span>Blogs</span><span>Contact Us</span>
  </nav>
  <div class="btn-login"><span class="badge"><svg width="12" height="12" viewBox="0 0 12 12"><rect x="5" y="1" width="5" height="10" fill="none" stroke="#2fae3c" stroke-width="1.2"/><path d="M1 6h5M4 4l2 2-2 2" fill="none" stroke="#2fae3c" stroke-width="1.2"/></svg></span>Login</div>
  <div class="btn-register"><span class="badge"><svg width="12" height="12" viewBox="0 0 12 12"><circle cx="6" cy="4" r="2.4" fill="none" stroke="#1b8fd0" stroke-width="1.2"/><path d="M1.5 11c0-3 2-4.3 4.5-4.3S10.5 8 10.5 11" fill="none" stroke="#1b8fd0" stroke-width="1.2"/></svg></span>Register</div>
</header>
<div class="brand-tab"><span class="mark"></span><span class="name">Keystone Home Sales</span></div>

<section class="hero">
  <h1 class="hero-title"><span class="line1">Welcome To</span><span class="line2">Keystone Home Sales</span></h1>
  <form class="valuation-form" aria-label="Sell your house today">
    <div class="form-title">Sell Your House Today – Tell Us About Your Property</div>
    <div class="field" style="left:5px"><label>Property Type</label><div class="input">select<span class="caret"></span></div></div>
    <div class="field" style="left:120px"><label>Address</label><div class="input">type here</div></div>
    <div class="field" style="left:235px"><label>Number of Bedrooms</label><div class="input">Select<span class="caret"></span></div></div>
    <div class="field" style="left:350px"><label>Estate Agents Valuation</label><div class="input">Select<span class="caret"></span></div></div>
    <div class="field" style="left:465px"><label>Best Price</label><div class="input">Select<span class="caret"></span></div></div>
    <div class="btn-search">Search</div>
  </form>
  <div class="hero-scene" role="img" aria-label="Illustration of houses for sale on grassy islands with a couple signing papers and an agent holding keys"></div>
</section>

<section class="why">
  <div class="skyline" role="img" aria-label="Faint city skyline illustration"></div>
  <h2 class="why-title">Why use us?</h2>

  <article class="reason-card" style="left:79px">
    <svg width="90" height="90" viewBox="0 0 110 110">
      <path d="M11.8 70.7A46 46 0 1 1 101 55" fill="none" stroke="#1b8fd0" stroke-width="8"/>
      <circle cx="11.8" cy="70.7" r="5" fill="#fff" stroke="#1b8fd0" stroke-width="2.5"/>
      <circle cx="55" cy="55" r="36" fill="#e4e5e8" stroke="#d3d5d9" stroke-width="1"/>
      <path d="M38 58l17-14 17 14M42 55v15h26V55" fill="none" stroke="#1b8fd0" stroke-width="2.5"/>
    </svg>
    <h3>Sell Your House</h3>
    <p>We will sell your house in 30 days and take a buyer's fee for our service from the buyer, meaning your buyer is secured, unlike with most estate agents.</p>
  </article>

  <article class="reason-card" style="left:319px">
    <svg width="90" height="90" viewBox="0 0 110 110">
      <path d="M9 55A46 46 0 1 0 98.2 39.3" fill="none" stroke="#1b8fd0" stroke-width="8"/>
      <circle cx="98.2" cy="39.3" r="5" fill="#fff" stroke="#1b8fd0" stroke-width="2.5"/>
      <circle cx="55" cy="55" r="36" fill="#e4e5e8" stroke="#d3d5d9" stroke-width="1"/>
      <circle cx="55" cy="55" r="17" fill="none" stroke="#1b8fd0" stroke-width="2.5"/>
      <path d="M43 67l24-24" stroke="#1b8fd0" stroke-width="2.5"/>
    </svg>
    <h3>No Sales Fees</h3>
    <p>We do not charge you any fees at all! Our small fee is charged to the buyer.</p>
  </article>

  <article class="reason-card" style="left:558px">
    <svg width="90" height="90" viewBox="0 0 110 110">
      <path d="M11.8 70.7A46 46 0 1 1 101 55" fill="none" stroke="#1b8fd0" stroke-width="8"/>
      <circle cx="11.8" cy="70.7" r="5" fill="#fff" stroke="#1b8fd0" stroke-width="2.5"/>
      <circle cx="55" cy="55" r="36" fill="#e4e5e8" stroke="#d3d5d9" stroke-width="1"/>
      <path d="M38 71h34M41 71V50h28v21M46 71V58M55 71V58M64 71V58M38 50l17-10 17 10" fill="none" stroke="#1b8fd0" stroke-width="2.5"/>
    </svg>
    <h3>UK Based</h3>
    <p>A huge network connecting many estate agents, auction houses, investors and private buyers across the UK to ensure a fast sale.</p>
  </article>

  <div class="btn-contact"><span class="badge"><svg width="16" height="10" viewBox="0 0 16 10"><path d="M1 5h13M10 1l4 4-4 4" fill="none" stroke="#1b8fd0" stroke-width="1.6"/></svg></span>Contact Us</div>
</section>

<footer class="site-footer">
  <div class="footer-brand"><span class="mark"></span><span class="name">Keystone Home Sales</span></div>
  <div class="social" aria-label="Social links"><span></span><span></span><span></span></div>

  <div class="footer-col" style="left:288px">
    <h4>Quick Links</h4>
    <ul><li>Home</li><li>About Us</li><li>Our Services</li><li>Blogs</li><li>Contact Us</li></ul>
  </div>
  <div class="footer-col" style="left:445px">
    <h4>Other Links</h4>
    <ul style="padding-left:6px"><li>FAQ</li><li>More</li></ul>
  </div>
  <div class="footer-col" style="left:606px">
    <h4 style="margin-left:4px">Contact Us</h4>
    <ul class="contact-list">
      <li><svg width="8" height="10" viewBox="0 0 8 10"><path d="M2 0.5h2l0.5 2.5-1.3 0.8c0.5 1.4 1 2 1.6 2.5l1.2-0.7 2 1.5-0.8 2.4C3 9 0.5 5 1 1.5z" fill="#fff"/></svg>+44 20 7946 0321</li>
      <li><svg width="8" height="11" viewBox="0 0 8 11"><path d="M4 0.5a3.5 3.5 0 0 1 3.5 3.5C7.5 6.5 4 10.5 4 10.5S0.5 6.5 0.5 4A3.5 3.5 0 0 1 4 0.5z" fill="#fff"/><circle cx="4" cy="4" r="1.3" fill="#17293a"/></svg>12 Harbour Lane,<br>Leeds LS1 4AB</li>
      <li><svg width="11" height="8" viewBox="0 0 11 8"><rect x="0.5" y="0.5" width="10" height="7" fill="#fff"/><path d="M0.5 0.5l5 4 5-4" fill="none" stroke="#17293a" stroke-width="1"/></svg>hello@keystonehomes<br>.example</li>
    </ul>
  </div>

  <div class="footer-rule"></div>
  <p class="copyright">Copyright ©2023 Keystone Home Sales . All Rights Reserved.</p>
</footer>

</body>
</html>
```